Video Company Business Card Design

We are looking for a new design for business cards that will complement our new logo and new website design.

Target Market(s)

professionals who need video work done

Industry/Entity Type

Business

Requirements
Must have
• Logo
compliment website look seen here...http://k7studiowerks.com/brightlens/

info for card:
Derek Halloway
Producer/ Cinematographer

462 Pendlemoor SW
Grand Rapids, MI 49504
(inside The VARN Center)
(555) 555-0174
Derek@brightlensfilms.com
www.brightlensfilms.com

```html
<!DOCTYPE html>
<html lang="en">
<head>
<meta charset="utf-8">
<title>Bright Lens Films – Business Card</title>
<link href="https://fonts.googleapis.com/css2?family=Didact+Gothic&display=swap" rel="stylesheet">
<style>
  :root {
    --stage: #2b2b2b;
    --card-top: #1c1c1c;
    --card-bottom: #050505;
    --frame: #8fdcaa;
    --brand-green: #2fa84f;
    --text-light: #f2f2f2;
    --text-soft: #d6d6d6;
  }
  * { margin: 0; padding: 0; box-sizing: border-box; }
  html, body {
    width: 1200px; height: 942px; overflow: hidden;
    background: var(--stage);
    font-family: "Didact Gothic", "Century Gothic", sans-serif;
  }
  .sheet { position: relative; width: 1200px; height: 942px; }
  .card {
    position: absolute; left: 250px; width: 700px; height: 400px;
    background: linear-gradient(160deg, var(--card-top), var(--card-bottom));
    box-shadow: 0 10px 30px rgba(0,0,0,.5);
  }
  .card--front { top: 50px; }
  .card--back { top: 492px; }
  .card__frame { position: absolute; inset: 12px; border: 3px solid var(--frame); }
  .brand {
    position: absolute; display: flex; align-items: center; gap: 12px;
    color: var(--brand-green); text-transform: uppercase; white-space: nowrap;
    font-weight: 400; letter-spacing: 0;
  }
  .brand__mark { width: 0.8em; height: 0.8em; background: var(--brand-green); }
  .card--front .brand { font-size: 56px; left: 50%; top: 50%; transform: translate(-50%, -50%); }
  .card--back .brand { font-size: 40px; left: 50%; top: 58px; transform: translateX(-50%); }
  .person { position: absolute; left: 78px; top: 190px; color: var(--text-light); }
  .person__name { font-size: 32px; font-weight: 400; line-height: 1; }
  .person__role { font-size: 12px; color: var(--text-soft); margin-top: 8px; }
  .address {
    position: absolute; right: 60px; top: 160px; text-align: right;
    color: var(--text-light); font-size: 17px; line-height: 1.3; font-style: normal;
  }
  .address__note { font-size: 12px; }
  .contacts {
    position: absolute; left: 78px; top: 262px; list-style: none;
    color: var(--text-light); font-size: 15px;
  }
  .contacts li { display: flex; align-items: center; gap: 16px; height: 32px; }
  .contacts svg { width: 20px; height: 20px; flex: none; }
</style>
</head>
<body>
<main class="sheet">
  <section class="card card--front" aria-label="Card front">
    <div class="card__frame"></div>
    <div class="brand"><span>Bright Lens Films</span><span class="brand__mark"></span></div>
  </section>

  <section class="card card--back" aria-label="Card back">
    <div class="card__frame"></div>
    <div class="brand"><span>Bright Lens Films</span><span class="brand__mark"></span></div>

    <div class="person">
      <h1 class="person__name">Derek Halloway</h1>
      <p class="person__role">Producer | Cinematographer</p>
    </div>

    <address class="address">
      462 Pendlemoor SW<br>
      Alder Bend ST 00417<br>
      <span class="address__note">(Inside The VARN Center)</span>
    </address>

    <ul class="contacts">
      <li>
        <svg viewBox="0 0 20 20" aria-hidden="true">
          <circle cx="10" cy="10" r="9" fill="none" stroke="#2fa84f" stroke-width="1.6"/>
          <path d="M7 5.5c-1 .6-1.4 2 -.6 4 .9 2.3 2.6 4.2 4.6 4.8 1.2.3 2-.2 2.3-.9l-1.6-1.4-1 .6c-1-.5-2-1.7-2.4-2.9l.9-.8-.9-2z" fill="#2fa84f"/>
        </svg>
        <span>(555) 555-0174</span>
      </li>
      <li>
        <svg viewBox="0 0 20 20" aria-hidden="true">
          <rect x="1.5" y="4.5" width="17" height="11" fill="none" stroke="#2fa84f" stroke-width="1.6"/>
          <path d="M1.5 4.5l8.5 6.5 8.5-6.5" fill="none" stroke="#2fa84f" stroke-width="1.6"/>
        </svg>
        <span>Derek@brightlensfilms.com</span>
      </li>
      <li>
        <svg viewBox="0 0 20 20" aria-hidden="true">
          <circle cx="10" cy="10" r="8.5" fill="none" stroke="#2fa84f" stroke-width="1.6"/>
          <ellipse cx="10" cy="10" rx="3.8" ry="8.5" fill="none" stroke="#2fa84f" stroke-width="1.3"/>
          <path d="M1.5 10h17M3 6h14M3 14h14" stroke="#2fa84f" stroke-width="1.2"/>
        </svg>
        <span>www.brightlensfilms.com</span>
      </li>
    </ul>
  </section>
</main>
</body>
</html>
```